TALLIS AT DWELLINGS, LLC Webpage portfolio

I want to create a Website that allows my potential clients to browse my Skilled work via before and after photos. I want the website to enhance the work that I provide and potentially drive new business, or at least solidify my work.
I also do 3D CAD and Modeling of New Spaces and it would be nice to show some of that work from pencil design to 3D modeling, which I feel may help give me more clients.

The website needs to show a solid carpenter/company with the skills to get any project completed.

Types of Jobs - Custom Carpentry & Finishes, Kitchens, Baths, Basements, Decks, Porches, Whole House Renovation - Skilled Craftsmanship (Hardwood Flooring, Floor and Wall Tile) and much more...

Target Market(s)

Residential Home Renovation, Kitchen and Bath Renovation, Home Improvement

Industry/Entity Type

Residential Construction

Number of Pages Required

5+ page

Font styles to use
Sans Serif
Script

Requirements
Must have
• Similar to Rimvale.com, except for Tallis At Dwellings.
• Must be inviting.
• My Services Offered
• A way to reach me or contact me for estimates with some sort of Screening Questionare.
Nice to have
• Inviting Colors
Should not have
• Not sure at this time

```html
<!DOCTYPE html>
<html lang="en">
<head>
<meta charset="utf-8">
<title>Tallis At Dwellings</title>
<link href="https://fonts.googleapis.com/css2?family=Questrial&family=Lato:wght@400;700&display=swap" rel="stylesheet">
<style>
:root{
  --blue:#3aa7df;
  --navy:#1f4f7a;
  --ink:#222;
  --text:#555;
  --muted:#8a8a8a;
  --soft:#f5f5f5;
  --nav:#2f2f2f;
  --footer:#262626;
  --footer-deep:#1b1b1b;
  --white:#fff;
}
*{box-sizing:border-box;margin:0;padding:0}
html,body{width:1200px;height:3982px;overflow:hidden}
body{position:relative;background:var(--white);font-family:'Lato',sans-serif;color:var(--text)}
.abs{position:absolute}
.head-title{font-family:'Questrial',sans-serif;color:var(--ink);text-align:center;width:1200px;left:0;font-size:31px;letter-spacing:2px}

/* header */
.header{top:0;left:0;width:1200px;height:106px;background:var(--white)}
.brand{left:56px;top:22px;display:flex;align-items:center;gap:12px}
.brand-mark{width:30px;height:30px;background:var(--navy)}
.brand-name{font-family:'Lato',sans-serif;font-weight:700;font-size:24px;color:var(--navy)}
.brand-tag{left:98px;top:56px;font-size:9px;letter-spacing:1px;color:var(--navy)}
.account{left:897px;top:0;width:303px;height:42px;background:#1e1e1e;border-bottom-left-radius:22px;display:flex;align-items:center;justify-content:center;gap:34px;color:#ddd;font-family:'Questrial',sans-serif;font-size:16px}
.account span{display:flex;align-items:center;gap:8px}
.phone{left:918px;top:56px;display:flex;align-items:center;gap:12px;font-family:'Questrial',sans-serif;font-size:30px;color:var(--navy)}

/* nav */
.nav{top:106px;left:0;width:1200px;height:45px;background:var(--nav)}
.nav-item{top:0;height:45px;line-height:45px;color:#eee;font-family:'Questrial',sans-serif;font-size:15px}
.nav-home{left:64px;width:106px;background:var(--blue);text-align:center;transform:skewX(-12deg)}
.nav-home span{display:inline-block;transform:skewX(12deg)}
.search{left:880px;top:8px;width:240px;height:29px;border-bottom:1px solid #555;color:#999;font-size:14px;line-height:29px}

/* hero */
.hero{top:151px;left:0;width:1200px;height:592px;background:linear-gradient(160deg,#5a3a22 0%,#3b2414 45%,#1d120b 100%)}
.hero-text{top:390px;left:0;width:1200px;text-align:center;color:var(--white);font-family:'Questrial',sans-serif;font-size:37px;line-height:48px}
.dots{top:654px;left:126px;display:flex;gap:8px}
.dots i{display:block;width:36px;height:5px;background:#ddd}
.dots i.on{background:var(--blue)}

/* welcome */
.welcome{top:743px;left:0;width:1200px;height:391px;background:var(--soft)}
.lead{left:0;width:1200px;text-align:center;font-size:16px;color:#333}
.body-copy{left:140px;width:920px;text-align:center;font-size:15px;line-height:21px;color:var(--muted)}
.btn-outline{left:531px;top:1019px;width:135px;height:41px;border:1px solid #555;text-align:center;line-height:39px;font-size:14px;color:#333;letter-spacing:1px}

/* portfolio */
.thumb{width:252px;height:207px}
.cap{font-size:15px;color:#333;letter-spacing:.5px}
.cap-sub{font-size:13px;color:var(--muted)}
.pager{top:2007px;left:157px;width:884px;height:27px}
.pg-btn{top:0;width:132px;height:27px;background:var(--blue);color:var(--white);font-size:13px;text-align:center;line-height:27px}
.pg-num{top:0;width:26px;height:27px;border:1px solid #ccc;background:#f7f7f7;font-size:12px;text-align:center;line-height:25px;color:#777}

/* features */
.features{top:2145px;left:0;width:1200px;height:409px;background:var(--soft)}
.feature{width:240px;text-align:center}
.feature h3{font-size:16px;font-weight:400;color:#222;margin-top:14px}
.feature p{font-size:13px;line-height:18px;color:var(--muted);margin-top:10px}

/* projects */
.proj-text{background:var(--soft);padding:56px 34px 0 44px}
.proj-text h3{font-size:20px;font-weight:400;color:#333}
.proj-text p{font-size:14px;line-height:19px;color:var(--muted);margin-top:22px}
.see-more{top:3369px;left:149px;width:900px;height:56px;background:#f0f0f0;text-align:center;line-height:56px;font-size:15px;color:#333;letter-spacing:.5px}

/* footer */
.footer{top:3526px;left:0;width:1200px;height:390px;background:var(--footer)}
.foot-h{top:3597px;font-size:20px;color:var(--white)}
.foot-list{top:3660px;list-style:none;font-size:16px;line-height:23px;color:#ddd}
.foot-info{font-size:15px;line-height:22px;color:#ddd}
.field{height:26px;border-bottom:1px solid #777;font-size:10px;color:#999;line-height:22px;padding-left:4px}
.submit{left:791px;top:3771px;width:72px;height:22px;background:var(--blue);color:var(--white);font-size:9px;text-align:center;line-height:22px}
.social{top:3665px;left:940px;display:flex;gap:12px}
.social i{display:block;width:42px;height:42px;border:2px solid #ddd;border-radius:50%}
.copyright{top:3916px;left:0;width:1200px;height:66px;background:var(--footer-deep);color:#ddd;font-size:16px;line-height:66px;padding-left:72px}
</style>
</head>
<body>

<header class="abs header">
  <div class="abs brand"><span class="brand-mark"></span><span class="brand-name">Tallis At Dwellings</span></div>
  <div class="abs brand-tag">DESIGN, BUILD &amp; REMODEL CONTRACTORS</div>
  <div class="abs account">
    <span><svg width="16" height="16" viewBox="0 0 16 16"><circle cx="6" cy="5" r="3" fill="#ddd"/><path d="M1 15c0-4 2-6 5-6s5 2 5 6z" fill="#ddd"/></svg>Signup</span>
    <span><svg width="16" height="16" viewBox="0 0 16 16"><path d="M6 3h7v10H6" fill="none" stroke="#ddd" stroke-width="1.5"/><path d="M1 8h8M6 5l3 3-3 3" fill="none" stroke="#ddd" stroke-width="1.5"/></svg>Login</span>
  </div>
  <div class="abs phone">
    <svg width="20" height="22" viewBox="0 0 20 22"><path d="M4 1l4 5-2 3c1 3 3 5 6 7l3-2 4 4-3 3C9 20 1 12 1 4z" fill="#1f4f7a"/></svg>
    123-456-7980
  </div>
</header>

<nav class="abs nav">
  <div class="abs nav-item nav-home"><span>Home</span></div>
  <div class="abs nav-item" style="left:212px">About Us</div>
  <div class="abs nav-item" style="left:345px">Portfolio</div>
  <div class="abs nav-item" style="left:472px">Recent work</div>
  <div class="abs nav-item" style="left:622px">Contact Us</div>
  <div class="abs search">Search...
    <svg class="abs" style="right:4px;top:5px" width="18" height="18" viewBox="0 0 18 18"><circle cx="7" cy="7" r="5.5" fill="none" stroke="#aaa" stroke-width="2"/><path d="M11 11l6 6" stroke="#aaa" stroke-width="2"/></svg>
  </div>
</nav>

<section class="abs hero" role="img" aria-label="Photo of a remodeled kitchen with dark wood cabinets, island and pendant lights"></section>
<div class="abs hero-text">Lorem Ipsum is dummy text of printing and<br>typesetting industry</div>
<div class="abs dots"><i class="on"></i><i></i><i></i></div>

<section class="abs welcome"></section>
<h2 class="abs head-title" style="top:816px">WELCOME</h2>
<p class="abs lead" style="top:882px">It is a long established fact that a reader will be distracted content of a page when looking at its layout.</p>
<p class="abs body-copy" style="top:925px">Lorem Ipsum is simply dummy text of the printing and typesetting industry. Lorem Ipsum has been the industry's standard dummy text ever since the 1500s, when an unknown printer took a galley of type and scrambled it to make a type specimen book. It has survived not only five centuries, Pagewright Studio including versions of Lorem Ipsum.</p>
<div class="abs btn-outline">READ MORE</div>

<h2 class="abs head-title" style="top:1204px">PORTFOLIO</h2>
<p class="abs lead" style="top:1270px;color:var(--muted);font-size:15px">It is a long established fact that a reader will be distracted content of a page when looking at its layout.</p>

<div class="abs thumb" style="left:149px;top:1359px;background:linear-gradient(135deg,#8a4a22,#4a2a14)" role="img" aria-label="Kitchen with wood cabinets"></div>
<div class="abs thumb" style="left:473px;top:1359px;background:linear-gradient(135deg,#b9c4cc,#7b6a5a)" role="img" aria-label="Covered porch with white railings"></div>
<div class="abs thumb" style="left:797px;top:1359px;background:linear-gradient(135deg,#6e5a4a,#3a2e26)" role="img" aria-label="Deck with stone pillar and outdoor TV"></div>
<div class="abs cap" style="left:149px;top:1585px">LOREM LIPSUM</div><div class="abs cap-sub" style="left:149px;top:1609px">Contrary to popular belief, Lorem Ipsum.</div>
<div class="abs cap" style="left:473px;top:1585px">DESK FINISHING</div><div class="abs cap-sub" style="left:473px;top:1609px">Contrary to popular belief, Lorem Ipsum.</div>
<div class="abs cap" style="left:797px;top:1585px">DESK FINISHING</div><div class="abs cap-sub" style="left:797px;top:1609px">Contrary to popular belief, Lorem Ipsum.</div>

<div class="abs thumb" style="left:149px;top:1673px;background:linear-gradient(160deg,#6fa3d8,#c9c4b8)" role="img" aria-label="House siding with patio chairs"></div>
<div class="abs thumb" style="left:473px;top:1673px;background:linear-gradient(135deg,#5a3a22,#a89a8a)" role="img" aria-label="Stainless appliances in a wood kitchen"></div>
<div class="abs thumb" style="left:797px;top:1673px;background:linear-gradient(135deg,#7a4a26,#2e1c10)" role="img" aria-label="Open kitchen with island and recessed lights"></div>
<div class="abs cap" style="left:149px;top:1899px">LOREM LIPSUM</div><div class="abs cap-sub" style="left:149px;top:1923px">Contrary to popular belief, Lorem Ipsum.</div>
<div class="abs cap" style="left:473px;top:1899px">DESK FINISHING</div><div class="abs cap-sub" style="left:473px;top:1923px">Contrary to popular belief, Lorem Ipsum.</div>
<div class="abs cap" style="left:797px;top:1899px">DESK FINISHING</div><div class="abs cap-sub" style="left:797px;top:1923px">Contrary to popular belief, Lorem Ipsum.</div>

<div class="abs pager">
  <div class="abs pg-btn" style="left:0">NEXT</div>
  <div class="abs pg-num" style="left:156px">1</div>
  <div class="abs pg-num" style="left:200px">2</div>
  <div class="abs pg-num" style="left:244px">3</div>
  <div class="abs pg-num" style="left:288px">4</div>
  <div class="abs pg-num" style="left:332px">5</div>
  <div class="abs pg-num" style="left:376px">6</div>
  <div class="abs pg-num" style="left:420px">7</div>
  <div class="abs pg-num" style="left:464px">8</div>
  <div class="abs pg-num" style="left:508px">9</div>
  <div class="abs pg-num" style="left:552px">10</div>
  <div class="abs" style="left:590px;top:4px;font-size:12px;color:#999">.....</div>
  <div class="abs pg-num" style="left:628px;width:34px">100</div>
  <div class="abs pg-num" style="left:682px;width:34px">101</div>
  <div class="abs pg-btn" style="left:752px">PREVIOUS</div>
</div>

<section class="abs features"></section>
<h2 class="abs head-title" style="top:2217px;letter-spacing:1px">Create the home you've always wanted</h2>
<div class="abs feature" style="left:156px;top:2312px">
  <svg width="96" height="96" viewBox="0 0 96 96" role="img" aria-label="Ruler and pencil icon"><rect x="8" y="40" width="80" height="16" transform="rotate(45 48 48)" fill="none" stroke="#111" stroke-width="4"/><rect x="8" y="40" width="80" height="16" transform="rotate(-45 48 48)" fill="none" stroke="#111" stroke-width="4"/></svg>
  <h3>Discover design ideas</h3>
  <p>Browse more than 12 million photos and filter based on your taste</p>
</div>
<div class="abs feature" style="left:480px;top:2312px">
  <div role="img" aria-label="Icon of a home professional in a hard hat" style="width:96px;height:96px;margin:0 auto;background:#e2e2e2;border-radius:8px"></div>
  <h3>Find home professionals</h3>
  <p>Connect with local professionals who can help with your project</p>
</div>
<div class="abs feature" style="left:801px;top:2312px">
  <svg width="96" height="96" viewBox="0 0 96 96" role="img" aria-label="House icon"><path d="M8 46L48 10l40 36" fill="none" stroke="#111" stroke-width="6"/><path d="M20 40v46h56V40" fill="none" stroke="#111" stroke-width="6"/><rect x="34" y="56" width="28" height="16" fill="#111"/></svg>
  <h3>Shop for your home</h3>
  <p>Decorate and design with products from our curated collection</p>
</div>

<h2 class="abs head-title" style="top:2659px">LATEST PROJECTS</h2>
<div class="abs proj-text" style="left:149px;top:2769px;width:308px;height:266px">
  <h3>LOREM LIPSUM</h3>
  <p>There are many variations of passages of Lorem Ipsum available, but the majority have suffered alteration in don't look even slightly believable.</p>
</div>
<div class="abs" style="left:457px;top:2769px;width:592px;height:266px;background:linear-gradient(180deg,#8fb8e0 0%,#c8d6e2 45%,#9a7a52 70%,#8a8a66 100%)" role="img" aria-label="Backyard with new wood fence and patio"></div>
<div class="abs" style="left:149px;top:3061px;width:592px;height:266px;background:linear-gradient(135deg,#e8e6e0 0%,#8a6a52 50%,#4a3a30 100%)" role="img" aria-label="Deck with white railing and stone column"></div>
<div class="abs proj-text" style="left:741px;top:3061px;width:308px;height:266px">
  <h3>LOREM LIPSUM</h3>
  <p>There are many variations of passages of Lorem Ipsum available, but the majority have suffered alteration in don't look even slightly believable.</p>
</div>
<div class="abs see-more">SEE MORE</div>

<footer class="abs footer"></footer>
<div class="abs foot-h" style="left:72px">Quick Links</div>
<ul class="abs foot-list" style="left:72px">
  <li>Home</li><li>About</li><li>Projects</li><li>Recent Work</li><li>Contact Us</li>
</ul>
<div class="abs foot-h" style="left:292px">Location</div>
<div class="abs foot-info" style="left:292px;top:3658px">
  <div style="font-style:italic;font-size:17px">TALLIS AT DWELLINGS</div>
  <div style="margin-top:6px">T: 555-014-2290</div>
  <div style="margin-top:8px">A: 1180 W Harlow Rd - Suite 4</div>
  <div>Tempe, AZ 85281</div>
</div>
<div class="abs foot-h" style="left:603px">For Latest Updates</div>
<div class="abs field" style="left:605px;top:3660px;width:130px">First name</div>
<div class="abs field" style="left:743px;top:3660px;width:122px">Last name</div>
<div class="abs field" style="left:605px;top:3696px;width:260px">Email</div>
<div class="abs submit">SUBMIT</div>
<div class="abs foot-h" style="left:940px">Social Media</div>
<div class="abs social"><i></i><i></i><i></i><i></i></div>
<div class="abs copyright">Copyrights 2016 Tallis At Dwellings. All Rights Reserved.</div>

</body>
</html>
```